Business Card Design

We need a business card for a new business based in Sydney, Australia. It is a home based baking business, the key products are cookies and muffins and slices including gluten free baked goods. With the emphasis on home made baking. The target market is cafes, coffee shops and vans, restaurants. Products may be provided in display jars or individually wrapped. The final design should be in the colours pink, purple.

Business

Tindle's Bakery Pty Ltd, Marisa Pellow, marisa@tindlesbakery.com.au
0451 276 308, www.tindlesbakery.com.au, ACN 512 648 397,

```html
<!DOCTYPE html>
<html lang="en">
<head>
<meta charset="utf-8">
<title>Tindle's Bakery Pty Ltd – Business Card</title>
<link rel="stylesheet" href="https://fonts.googleapis.com/css2?family=Lobster&family=Montserrat:wght@600&family=Dancing+Script:wght@500&family=Maven+Pro:wght@400&display=swap">
<style>
  :root {
    --pink: #f752ae;
    --purple: #4a00a0;
    --label-black: #222222;
    --ink: #2a2a2a;
    --white: #ffffff;
    --lilac: #c9b8ec;
  }
  html, body {
    margin: 0;
    padding: 0;
    overflow: hidden;
    background: #e9e9e9;
  }
  .card {
    position: relative;
    width: 741px;
    height: 1200px;
    background: var(--purple);
    overflow: hidden;
  }
  .pattern-band {
    position: absolute;
    left: 0;
    top: 0;
    width: 741px;
    height: 593px;
    background: var(--pink);
  }
  .business-name {
    position: absolute;
    left: 0;
    width: 741px;
    top: 112px;
    margin: 0;
    text-align: center;
    font-family: "Lobster", cursive;
    font-weight: 400;
    font-size: 62px;
    line-height: 1;
    color: var(--ink);
    text-shadow: 2px 3px 4px rgba(0,0,0,0.35);
  }
  .person-name {
    position: absolute;
    left: 0;
    width: 741px;
    top: 200px;
    margin: 0;
    text-align: center;
    font-family: "Montserrat", sans-serif;
    font-weight: 600;
    font-size: 28px;
    line-height: 1;
    color: var(--ink);
  }
  .call-label {
    position: absolute;
    left: 0;
    top: 0;
    width: 741px;
    height: 1200px;
  }
  .call-heading {
    position: absolute;
    left: 170px;
    top: 500px;
    margin: 0;
    font-family: "Dancing Script", cursive;
    font-weight: 500;
    font-size: 100px;
    line-height: 1;
    color: var(--white);
    text-shadow: 2px 3px 3px rgba(0,0,0,0.5);
  }
  .call-number {
    position: absolute;
    left: 170px;
    top: 648px;
    margin: 0;
    font-family: "Maven Pro", sans-serif;
    font-size: 43px;
    line-height: 1;
    color: var(--white);
    letter-spacing: 0.5px;
  }
  .contact-lines {
    position: absolute;
    left: 182px;
    top: 900px;
    margin: 0;
    font-family: "Maven Pro", sans-serif;
    font-size: 32px;
    line-height: 43px;
    color: var(--white);
  }
  .contact-lines .web { padding-left: 7px; }
  .company-number {
    position: absolute;
    left: 0;
    width: 741px;
    top: 1118px;
    margin: 0;
    text-align: center;
    font-family: "Maven Pro", sans-serif;
    font-size: 24px;
    line-height: 1;
    color: var(--lilac);
  }
</style>
</head>
<body>
  <div class="card">
    <div class="pattern-band" role="img" aria-label="Pink polka dot pattern background"></div>

    <h1 class="business-name">Tindle's Bakery Pty Ltd</h1>
    <p class="person-name">Marisa Pellow</p>

    <svg class="call-label" viewBox="0 0 741 1200" aria-hidden="true">
      <g transform="scale(1.0818)">
        <path fill="var(--label-black)"
          d="M35,462 C120,470 200,455 250,445 C270,430 310,430 330,445 C380,455 460,470 548,462 C540,500 560,540 572,573 C560,610 540,650 552,687 C460,680 380,690 330,702 C310,720 270,720 250,702 C200,690 120,680 30,687 C42,650 22,610 10,573 C22,540 42,500 35,462 Z"/>
        <path fill="none" stroke="var(--white)" stroke-width="1.6" stroke-dasharray="5 4"
          vector-effect="non-scaling-stroke"
          transform="translate(291,575) scale(0.92,0.86) translate(-291,-575)"
          d="M35,462 C120,470 200,455 250,445 C270,430 310,430 330,445 C380,455 460,470 548,462 C540,500 560,540 572,573 C560,610 540,650 552,687 C460,680 380,690 330,702 C310,720 270,720 250,702 C200,690 120,680 30,687 C42,650 22,610 10,573 C22,540 42,500 35,462 Z"/>
      </g>
    </svg>

    <h2 class="call-heading">Call us</h2>
    <p class="call-number">0451 276 308</p>

    <p class="contact-lines">
      <span class="email">marisa@tindlesbakery.com.au</span><br>
      <span class="web">www.tindlesbakery.com.au</span>
    </p>

    <p class="company-number">ACN 512 648 397</p>
  </div>
</body>
</html>
```